Legal Campaign

A courier compavny that offer Legal services like filing/recording Court documents.

These info must be on card: Can We Help With Your Legal Services? Need Your Court documents quickly filed? .Filing/Recording in Erie, Niagara & Monroe County .Pick-up within 15-30 minutes of call .Medical records pick-up & delivery .Court-Authorized Process Servers .$9.00 Buffalo to Buffalo .Volume Discounts Call Liam Torvane@716-555-0148 The address must be 47 Harlow Ave., Buffalo NY 14209

Please add the following info: 1.Post Office Pickup/Deliveries 2. Liamtorvane@brisktrn.com

Target Market(s)

Law firms & legal community.

Industry/Entity Type

Court

Requirements
Must have
• SwiftHaulo logo must be on card. Please visit the website@brisktrn.com to check out the logo. Thanks

```html
<!DOCTYPE html>
<html lang="en">
<head>
<meta charset="utf-8">
<title>SwiftHaulo Legal Courier Services</title>
<link rel="stylesheet" href="https://fonts.googleapis.com/css2?family=Open+Sans:ital,wght@0,400;0,600;0,700;1,700&display=swap">
<style>
  :root {
    --brand-blue: #1459a8;
    --deep-blue: #0d4a92;
    --accent-orange: #f28a1e;
    --ink: #2b2b2b;
    --paper: #ffffff;
    --photo-light: #e6edf3;
    --photo-mid: #a9bccd;
  }
  html, body {
    margin: 0;
    padding: 0;
    width: 1200px;
    height: 948px;
    overflow: hidden;
    background: var(--paper);
  }
  .flyer {
    position: relative;
    width: 1200px;
    height: 948px;
    overflow: hidden;
    font-family: "Open Sans", Arial, sans-serif;
    color: var(--ink);
  }
  .flyer-shapes {
    position: absolute;
    inset: 0;
  }
  .headline {
    position: absolute;
    left: 0;
    width: 1200px;
    margin: 0;
    text-align: center;
    font-style: italic;
    font-weight: 700;
    font-size: 42px;
    line-height: 1;
    color: var(--ink);
  }
  .headline-top { top: 96px; }
  .headline-bottom { top: 170px; }
  .headline .accent-orange { color: var(--accent-orange); }
  .headline .accent-blue { color: var(--brand-blue); }
  .offer-title {
    position: absolute;
    left: 46px;
    top: 286px;
    margin: 0;
    font-size: 31px;
    font-weight: 700;
    color: var(--brand-blue);
  }
  .offer-title .accent-orange { color: var(--accent-orange); }
  .offer-list {
    position: absolute;
    left: 52px;
    top: 358px;
    width: 560px;
    margin: 0;
    padding: 0;
    list-style: none;
    font-size: 27px;
    line-height: 43px;
  }
  .offer-list li {
    position: relative;
    padding-left: 22px;
    margin-bottom: 34px;
  }
  .offer-list li::before {
    content: "";
    position: absolute;
    left: 0;
    top: 18px;
    width: 8px;
    height: 8px;
    border-radius: 50%;
    background: var(--brand-blue);
  }
  .brand-name {
    position: absolute;
    left: 793px;
    top: 752px;
    width: 372px;
    margin: 0;
    text-align: center;
    font-size: 58px;
    font-weight: 700;
    line-height: 1;
    color: var(--paper);
  }
  .contact {
    position: absolute;
    left: 654px;
    top: 858px;
    margin: 0;
    font-size: 27px;
    line-height: 40px;
    color: var(--paper);
  }
  .contact .phone {
    font-weight: 700;
    margin-left: 8px;
  }
  .contact svg {
    vertical-align: -4px;
    margin-left: 10px;
  }
  .office-details {
    position: absolute;
    left: 40px;
    top: 872px;
    margin: 0;
    font-size: 18px;
    line-height: 24px;
    color: var(--paper);
  }
</style>
</head>
<body>
<main class="flyer">
  <svg class="flyer-shapes" width="1200" height="948" viewBox="0 0 1200 948">
    <defs>
      <radialGradient id="photoTone" cx="40%" cy="40%" r="70%">
        <stop offset="0%" stop-color="#e6edf3"/>
        <stop offset="100%" stop-color="#a9bccd"/>
      </radialGradient>
    </defs>
    <rect class="backdrop" width="1200" height="948" fill="var(--brand-blue)"/>
    <path class="content-field" fill="var(--paper)"
      d="M190 0 L1010 0 C1110 30 1170 80 1200 120 L1200 540 C1000 640 700 740 300 780 C200 790 100 785 0 770 L0 200 C40 110 100 40 190 0 Z"/>
    <path class="swoosh-orange" fill="var(--accent-orange)"
      d="M0 170 C70 80 190 20 330 0 L370 0 C220 30 90 90 0 200 Z"/>
    <path class="swoosh-blue" fill="var(--deep-blue)"
      d="M0 120 C50 60 110 20 170 0 L230 0 C140 40 60 100 0 160 Z"/>
    <path class="swoosh-orange" fill="var(--accent-orange)"
      d="M880 0 L960 0 C1080 30 1160 80 1200 130 L1200 170 C1150 100 1040 40 880 0 Z"/>
    <path class="swoosh-orange" fill="var(--accent-orange)"
      d="M1200 525 C1000 625 700 722 300 768 C200 780 120 783 60 780 C130 798 220 800 320 790 C720 750 1010 650 1200 565 Z"/>
    <path class="band-white" fill="var(--paper)"
      d="M0 812 C200 850 450 850 740 800 C460 868 200 872 0 838 Z"/>
    <ellipse cx="884" cy="470" rx="276" ry="212" fill="var(--paper)"/>
    <ellipse class="photo-slot" role="img" aria-label="Photo of stacked legal documents with reading glasses and a pencil"
      cx="884" cy="470" rx="264" ry="200" fill="url(#photoTone)"/>
  </svg>

  <h1 class="headline headline-top">Can We Help With Your <span class="accent-orange">Legal Services</span>?</h1>
  <h2 class="headline headline-bottom">Need Your Court <span class="accent-blue">documents quickly filed</span>?</h2>

  <h3 class="offer-title"><span class="accent-orange">WE</span> OFFER</h3>
  <ul class="offer-list">
    <li>Filing/Recording in Erie, Niagara &amp;<br>Monroe County</li>
    <li>Pick-up within 15-30 minutes of call</li>
    <li>Medical records pick-up &amp; delivery</li>
    <li>Court-Authorized Process Servers</li>
    <li>$9.00 Buffalo to Buffalo</li>
  </ul>

  <p class="brand-name">SwiftHaulo</p>

  <p class="office-details">
    Post Office Pickup/Deliveries<br>
    47 Harlow Ave., Buffalo NY 14209<br>
    Liamtorvane@brisktrn.com
  </p>

  <p class="contact">
    Volume Discounts<br>
    Call Liam Torvane<svg width="24" height="24" viewBox="0 0 24 24" aria-hidden="true"><path fill="#ffffff" d="M6.6 10.8c1.4 2.8 3.8 5.1 6.6 6.6l2.2-2.2c.3-.3.7-.4 1-.2 1.1.4 2.300.6 3.600.6.6 0 1 .4 1 1V20c0 .6-.4 1-1 1C10.6 21 3 13.4 3 4c0-.6.4-1 1-1h3.5c.6 0 1 .4 1 1 0 1.3.2 2.5.6 3.6.1.3 0 .7-.2 1z"/></svg><span class="phone">716-555-0148</span>
  </p>
</main>
</body>
</html>
```